Company Broshure Oil&Energy Industry

We have recently completed a company rebranding, and our new website is now fully live and available at www.velmorquist.ro.

To ensure consistency across all communication materials, we would like to redesign our company presentation flyer/brochure so that it fully reflects the updated branding and visual identity of the website.

Please find attached our current brochure (last item uploaded on the list), which should be redesigned in line with the new website’s look and feel. The overall structure and text content should remain unchanged; only the layout and visual design need to be updated. I have uploaded pictures from of the website theme. Can be used by designers for the new design.
Updates

We uploaded pictures belonging to website design theme that can be used for the new brochure.

Target Market(s)

EPC Contractors

Industry/Entity Type

Oil&Energy

Font styles to use
Other font styles liked:
• Calibri

Colors
0094D4
00A9DD
6FCCEA
C7EBF8
E9F6FB

Requirements
Must have
• a clear structure, elegant layout
Nice to have
• I would like to have a dynamic approach. To feel elegant and alive.

```html
<!DOCTYPE html>
<html lang="en">
<head>
<meta charset="utf-8">
<title>Velmorquist Group – Company Brochure</title>
<link href="https://fonts.googleapis.com/css2?family=Raleway:wght@500;600;700&family=Carlito:ital,wght@0,400;0,700;1,400&display=swap" rel="stylesheet">
<style>
:root{
  --navy:#0b2f52;
  --navy-light:#0f4a78;
  --teal-dark:#1d6b74;
  --teal-text:#1a6b78;
  --blue:#0094d4;
  --blue-2:#00a9dd;
  --sky:#6fccea;
  --ice:#c7ebf8;
  --mist:#e9f6fb;
  --white:#ffffff;
  --ink:#2a3a44;
  --bg:#e8e5e0;
}
*{margin:0;padding:0;box-sizing:border-box}
html,body{width:1200px;height:800px;overflow:hidden}
body{background:var(--bg);font-family:"Carlito",Calibri,sans-serif;color:var(--ink);position:relative}
.spread{position:absolute;left:30px;width:1140px;height:357px;box-shadow:0 2px 8px rgba(0,0,0,.25)}
.spread--outer{top:30px;display:flex}
.spread--inner{top:413px;display:flex;gap:4px;box-shadow:none}
.page{position:relative;height:357px;overflow:hidden}
.spread--outer .page{width:570px}
.spread--inner .page{width:568px;background:var(--white);box-shadow:0 2px 8px rgba(0,0,0,.25)}
.layer{position:absolute;inset:0}
.head{font-family:"Raleway",sans-serif;font-weight:600;position:absolute}

/* contact page */
.contact{background:var(--navy)}
.contact__title{left:48px;top:44px;font-size:21px;color:var(--white)}
.contact__list{position:absolute;left:90px;top:82px;color:var(--white);font-size:8px;font-weight:700;line-height:1.2}
.contact__list p{margin-bottom:7px}
.contact__list .gap{margin-top:12px}
.icon{position:absolute}
.contact__photo{position:absolute;left:3px;top:218px;width:562px;height:113px;background:linear-gradient(90deg,#6e6a63,#b9aa98 40%,#c9c1b5 60%,#8c8276)}

/* cover page */
.cover{background:linear-gradient(120deg,#1a5f8f 0%,#1b86b9 45%,#19a6d8 100%)}
.cover__title{right:30px;top:26px;font-size:21px;color:var(--white);font-weight:700}
.cover__band{position:absolute;left:0;right:0;top:289px;height:51px;background:rgba(10,52,88,.78)}
.cover__foot{position:absolute;left:0;right:0;top:340px;height:17px;background:#1a6e9e}
.brand-mark{font-family:"Raleway",sans-serif;font-weight:600;color:var(--white)}
.cover__mark{position:absolute;right:24px;top:296px;font-size:32px;letter-spacing:1px}

/* inner left */
.who{position:absolute;left:25px;color:var(--white)}
.who__mark{top:138px;font-size:19px}
.who__title{left:25px;top:176px;font-size:14px;color:var(--white)}
.who__text{top:204px;font-size:5.4px;line-height:1.3;white-space:nowrap}
.who__text p{margin-bottom:6px}
.services__title{left:0;width:100%;text-align:center;padding-left:140px;top:20px;font-size:15px;color:var(--teal-text)}
.svc{position:absolute;color:var(--white);font-size:6px;text-align:center;line-height:1.2}
.svc b{font-weight:700;display:block}
.svc span{font-size:5.3px}
.rule{position:absolute;width:1px;background:rgba(255,255,255,.85)}
.industry__title{left:206px;top:176px;font-size:14.5px;color:var(--teal-text)}
.industry__text{position:absolute;left:208px;top:208px;width:160px;font-size:5.6px;line-height:1.25;text-align:center}
.industry__text p{margin-bottom:7px}
.sectors{position:absolute;left:0;top:0;font-family:"Raleway",sans-serif;font-weight:600;font-size:10.5px;color:var(--teal-text)}
.sectors li{position:absolute;list-style:none;white-space:nowrap}
.sectors li::before,.phases li::before{content:"";display:inline-block;width:0;height:0;border-left:2.5px solid transparent;border-right:2.5px solid transparent;border-bottom:5px solid var(--blue-2);margin-right:4px;vertical-align:1px}

/* inner right */
.phases__title{left:34px;top:20px;font-size:15px;line-height:1.2;color:var(--teal-text)}
.phases{position:absolute;left:38px;top:101px;list-style:none;font-family:"Raleway",sans-serif;font-weight:600;font-size:11px;color:var(--teal-text);line-height:18.3px}
.phases__note{position:absolute;left:30px;top:248px;width:106px;font-size:7px;text-align:center;line-height:1.15;color:var(--teal-text)}
.block__title{font-size:14.5px;color:var(--teal-text)}
.block__text{position:absolute;font-size:5.6px;line-height:1.25;text-align:justify}
.when__title{left:198px;top:19px}
.when__text{left:296px;top:22px;width:244px}
.philo__title{left:223px;top:84px}
.philo__text{left:344px;top:88px;width:196px;font-style:italic}
.philo__sign{position:absolute;right:30px;top:148px;font-size:5.6px;font-weight:700}
.ref__title{left:260px;top:178px}
.ref__text{left:348px;top:182px;width:192px}
.partner{position:absolute;background:#c9d2d8}
</style>
</head>
<body>

<section class="spread spread--outer">
  <div class="page contact">
    <svg class="layer" width="570" height="357" aria-hidden="true">
      <polygon points="399,0 570,0 570,357 558,357" fill="var(--navy-light)"/>
    </svg>
    <h2 class="head contact__title">Contact</h2>
    <svg class="icon" style="left:50px;top:78px" width="26" height="24" viewBox="0 0 26 24" aria-hidden="true">
      <path d="M4 3h4v3H5v14h7" fill="none" stroke="var(--blue-2)" stroke-width="2"/>
      <rect x="10" y="10" width="14" height="10" fill="none" stroke="var(--blue-2)" stroke-width="1.6"/>
      <path d="M10 10l7 5 7-5" fill="none" stroke="var(--blue-2)" stroke-width="1.6"/>
    </svg>
    <svg class="icon" style="left:54px;top:118px" width="18" height="28" viewBox="0 0 18 28" aria-hidden="true">
      <path d="M9 0C4 0 0 4 0 9c0 7 9 19 9 19s9-12 9-19c0-5-4-9-9-9z" fill="var(--blue-2)"/>
      <circle cx="9" cy="9" r="3.5" fill="var(--navy)"/>
    </svg>
    <div class="contact__list">
      <p>Email: office@velmorquist.ro</p>
      <p>Website: www.velmorquist.ro</p>
      <p class="gap">Str. Fabricii Noi, no.7<br>Bucharest, Romania</p>
      <p class="gap">Tel:0040700555219</p>
    </div>
    <div class="contact__photo" role="img" aria-label="Photo of a young woman smiling while working on a laptop in a bright office"></div>
  </div>

  <div class="page cover">
    <div class="layer" role="img" aria-label="Photo of a glass office tower under construction with workers on scaffolding, tinted blue" style="background:linear-gradient(160deg,rgba(20,80,120,.55),rgba(25,150,200,.15) 60%,rgba(30,180,220,.2))"></div>
    <svg class="layer" width="570" height="357" aria-hidden="true">
      <polygon points="0,0 95,0 250,357 0,357" fill="rgba(40,200,210,.22)"/>
    </svg>
    <div class="cover__band"></div>
    <div class="cover__foot"></div>
    <h1 class="head cover__title">Velmorquist Grup</h1>
    <div class="brand-mark cover__mark">VMQ</div>
  </div>
</section>

<section class="spread spread--inner">
  <div class="page">
    <svg class="layer" width="568" height="357" aria-hidden="true">
      <defs>
        <linearGradient id="svcBand" x1="0" x2="1" y1="0" y2="0">
          <stop offset="0" stop-color="#0a56a3"/>
          <stop offset=".55" stop-color="#0a86b8"/>
          <stop offset="1" stop-color="#18b6b6"/>
        </linearGradient>
      </defs>
      <polygon points="0,0 89,0 255,357 0,357" fill="var(--teal-dark)"/>
      <polygon points="134,46 568,46 568,161 188,161" fill="url(#svcBand)"/>
    </svg>
    <h2 class="head services__title">Services</h2>
    <div class="svc" style="left:180px;top:64px;width:68px"><b>Discipline Site Supervision</b><span>(mechanical, electric, I&amp;C, piping)</span></div>
    <div class="rule" style="left:256px;top:64px;height:30px"></div>
    <div class="svc" style="left:264px;top:64px;width:70px"><b>Site Management</b><span>(Construction/Commissioning)</span></div>
    <div class="rule" style="left:344px;top:64px;height:30px"></div>
    <div class="svc" style="left:350px;top:64px;width:98px"><b>Project Service Management</b><span>(Planning, Cost Control/Estimate, Project Control, Document Controlling, Contract Control, Procurement)</span></div>
    <div class="rule" style="left:466px;top:64px;height:30px"></div>
    <div class="svc" style="left:474px;top:64px;width:80px"><b>Quality Control, Quality Assurance</b></div>
    <div class="svc" style="left:220px;top:126px;width:70px"><b>HSE supervision, HSE Management</b></div>
    <div class="rule" style="left:300px;top:121px;height:32px"></div>
    <div class="svc" style="left:306px;top:126px;width:96px"><b>Welding &amp; NDT inspections</b></div>
    <div class="rule" style="left:420px;top:121px;height:32px"></div>
    <div class="svc" style="left:428px;top:126px;width:96px"><b>Discipline Engineering</b><span>(process, piping, stress piping, instrument, electric, civil)</span></div>

    <div class="brand-mark who who__mark">VMQ</div>
    <h2 class="head who__title">Who We Are</h2>
    <div class="who who__text">
      <p>Velmorquist Group is a Romanian<br>registred company, founded in 2003.</p>
      <p>We have been active in Oil&amp;Energy industry<br>serving local and international market by sourcing<br>highly specilised professionals for Oil&amp;Energy<br>projects.</p>
      <p>We offer a wide range of services that encompass<br>every stage of the process, starting from the initial<br>selection of professionals and extending to the<br>management of employment and logistics (mobilisation)<br>for the assigned resources. Whether the project is located<br>domestically or abroad, we offer tailored support to ensure<br>successful project completion for our clients</p>
    </div>

    <h2 class="head industry__title">Industry We Serve</h2>
    <div class="industry__text">
      <p>We are active in Oil&amp; Energy sector with hands on experience in upstream and downstream projects either brown or green field.</p>
      <p>Over the years we got involved in various projects within Refineries, LNG-s, Pipelines, Offshore Platforms, Power Plants (simple or combined cycle), Nuclear Power Plants and not least renewable from solar to wind or biomass.</p>
      <p>Having a large network of Romanian specialists available for mobilisation for projects inland and across the globe, we can respond quickly to clients' requests by proposing the best available resources on the market</p>
    </div>
    <ul class="sectors">
      <li style="left:402px;top:177px">OIL&amp;GAS</li>
      <li style="left:412px;top:195px">POWER</li>
      <li style="left:422px;top:213px">PETROCHEMISTRY</li>
      <li style="left:446px;top:231px">PHARMA</li>
    </ul>
    <svg class="layer" width="568" height="357" role="img" aria-label="Photo of two engineers in white hard hats at an industrial site">
      <defs>
        <linearGradient id="engPhoto" x1="0" x2="1">
          <stop offset="0" stop-color="#c9b7aa"/>
          <stop offset=".45" stop-color="#b0413b"/>
          <stop offset="1" stop-color="#d9d6d0"/>
        </linearGradient>
      </defs>
      <polygon points="424,264 568,264 568,357 468,357" fill="url(#engPhoto)"/>
    </svg>
  </div>

  <div class="page">
    <svg class="layer" width="568" height="357" aria-hidden="true">
      <defs>
        <linearGradient id="mistFade" x1="0" y1="0" x2="1" y2=".4">
          <stop offset="0" stop-color="var(--white)"/>
          <stop offset=".6" stop-color="var(--mist)"/>
          <stop offset="1" stop-color="#a9e0e4"/>
        </linearGradient>
        <linearGradient id="stairPhoto" x1="0" x2="1">
          <stop offset="0" stop-color="#dfe3e4"/>
          <stop offset=".5" stop-color="#eef0f0"/>
          <stop offset="1" stop-color="#d5d9db"/>
        </linearGradient>
      </defs>
      <polygon points="0,0 135,0 158,48 145,48 145,357 0,357" fill="url(#mistFade)"/>
      <polygon points="145,48 158,48 312,357 145,357" fill="url(#stairPhoto)" role="img" aria-label="Photo of workers in orange high-visibility gear climbing white outdoor stairs"/>
    </svg>
    <h2 class="head phases__title">Project<br>Phases<br>We Cover</h2>
    <ul class="phases">
      <li>Engineering</li>
      <li>Construction</li>
      <li>Commissioning</li>
      <li>Start-up &amp;</li>
      <li>Operation</li>
      <li>Maintenance</li>
      <li>Operation</li>
    </ul>
    <p class="phases__note">VMQ is able to assit you along project life time by offering the key resources needed to complete and run the project.</p>

    <h2 class="head block__title when__title">When VMQ?</h2>
    <p class="block__text when__text">Whether you require a seasoned expert or a specialized team for your project, or if you're seeking to enhance your existing team with the right talent, we are here to assist. Velmorquist Group is dedicated to your project team efficiently and cost-effectively!</p>

    <h2 class="head block__title philo__title">Our Philosophy</h2>
    <p class="block__text philo__text">Daily, we realize the world is remarkably interconnected. With decades of experience, we've come to appreciate the enduring value of human relationships—much like fine wine, they grow richer with time. Through our journey, we've cultivated a robust network of trusted professionals who rely on us just as much as we rely on them. Despite the inevitable mistakes we've made, each one served a purpose, guiding us towards improvement. Ultimately, it's our reputation that speaks volumes about the quality of our service.</p>
    <p class="philo__sign">- Ilinca Moraru</p>

    <h2 class="head block__title ref__title">Refferences</h2>
    <p class="block__text ref__text">We are collaborating with esteemed EPC contractors, Owners, and Engineering companies, offering comprehensive teams for durations ranging from 3 to 6 months or longer. Our support is essential during crucial phases such as turnarounds, construction, or commissioning. VMQ provides the necessary expertise and manpower to expedite ongoing projects, ensuring timely completion for our clients.</p>

    <div class="partner" style="left:316px;top:245px;width:44px;height:18px"></div>
    <div class="partner" style="left:372px;top:245px;width:56px;height:18px"></div>
    <div class="partner" style="left:444px;top:247px;width:88px;height:14px"></div>
    <div class="partner" style="left:318px;top:287px;width:24px;height:24px;border-radius:50%"></div>
    <div class="partner" style="left:360px;top:290px;width:46px;height:18px"></div>
    <div class="partner" style="left:420px;top:292px;width:46px;height:14px"></div>
    <div class="partner" style="left:480px;top:290px;width:60px;height:16px"></div>
  </div>
</section>

</body>
</html>
```